Cedar Hollow Drift Tours

We offer guided cross country ( Nordic ) skiing tours in the National Forest bordering Yellowstone National Park. I need a website that attracts individuals by using photos ( provided by me ) , brief descriptions of what to expect, a place with phone numbers to call for a tour, and I would like the website to feature the same color scheme as the logo, which I will upload.

```html
<!DOCTYPE html>
<html lang="en">
<head>
<meta charset="utf-8">
<title>Cedar Hollow Drift Tours</title>
<link rel="stylesheet" href="https://fonts.googleapis.com/css2?family=Roboto+Condensed:wght@400;700&family=Montserrat:ital,wght@0,400;0,500;1,400&family=Kaushan+Script&display=swap">
<style>
:root{
  --yellow:#f9b800;
  --dark:#1b1b1b;
  --footer:#222222;
  --white:#ffffff;
  --ink:#1e1e1e;
  --muted:#555555;
  --outline-dark:#3c3c3c;
  --outline-light:#c9c9c9;
}
*{margin:0;padding:0;box-sizing:border-box}
html,body{width:1200px;height:4257px;overflow:hidden}
body{position:relative;background:var(--white);font-family:"Montserrat",sans-serif;color:var(--ink)}
.abs{position:absolute}
.center{transform:translateX(-50%);white-space:nowrap;text-align:center}
.cond{font-family:"Roboto Condensed",sans-serif;font-weight:700}
.btn{position:absolute;background:var(--yellow);color:var(--ink);font-family:"Roboto Condensed",sans-serif;font-weight:700;font-size:15px;display:flex;align-items:center;justify-content:center;text-transform:uppercase}
.outline-word{position:absolute;left:600px;transform:translateX(-50%);font-family:"Roboto Condensed",sans-serif;font-weight:400;color:transparent;white-space:nowrap;line-height:1}

/* Hero */
.hero{position:absolute;left:0;top:0;width:1200px;height:640px;background:linear-gradient(180deg,#38443d 0%,#56625a 25%,#8d9794 45%,#c9cdcf 62%,#eef0f2 80%,#ffffff 100%)}
.nav-band{position:absolute;left:0;top:50px;width:1200px;height:44px;background:rgba(30,30,30,.45)}
.nav-link{position:absolute;top:63px;color:var(--white);font-size:14px;font-weight:500;transform:translateX(-50%)}
.nav-link.active::after{content:"";position:absolute;left:0;right:0;bottom:-14px;height:2px;background:var(--white)}
.brand{position:absolute;left:600px;top:40px;transform:translateX(-50%);display:flex;align-items:center;gap:8px;color:var(--white);font-size:12px;font-weight:500;line-height:1.25}
.brand-dot{width:22px;height:22px;border-radius:50%;background:var(--white)}
.hero-title{position:absolute;left:600px;top:245px;transform:translateX(-50%);text-align:center;color:var(--white);font-family:"Roboto Condensed",sans-serif;font-weight:700;font-size:92px;line-height:102px;white-space:nowrap}
.hero-title .script{font-family:"Kaushan Script",cursive;font-weight:400;color:var(--yellow);font-size:86px}
.side-nav{position:absolute;top:344px;color:var(--white);font-size:13px;letter-spacing:1px}
.side-line{position:absolute;top:344px;height:1px;width:66px;background:var(--white)}

/* About */
.eyebrow{font-size:15px;letter-spacing:4px}
.about-title{position:absolute;left:71px;top:792px;font-size:54px;line-height:60px;color:var(--ink)}
.about-text{position:absolute;left:522px;top:790px;width:610px;font-size:14.5px;line-height:23px;color:var(--muted)}

/* Services */
.services{position:absolute;left:0;top:1098px;width:1200px;height:646px;background:var(--dark)}
.yellow-eyebrow{color:var(--yellow);font-size:15px;letter-spacing:4px}
.section-title{font-size:50px;color:var(--white);line-height:1}
.dest{position:absolute;top:1336px;width:244px;height:244px;border-radius:50%;border:1.5px solid #3a3a3a}
.dest-photo{position:absolute;left:11px;top:11px;width:220px;height:220px;border-radius:50%}
.dest-name{position:absolute;top:1596px;color:var(--white);font-size:20px}

/* Gallery */
.gallery-photo{position:absolute;top:1952px;width:400px;height:356px}
.chev{position:absolute;top:2094px}

/* Testimonial */
.quote{position:absolute;left:600px;top:2506px;transform:translateX(-50%);text-align:center;font-style:italic;font-size:27px;line-height:39px;color:#2a2a2a;width:760px}

/* Blog */
.blog{position:absolute;left:0;top:2810px;width:1200px;height:557px;background:linear-gradient(180deg,#1f1f1f,#141414)}
.card-photo{position:absolute;top:3008px;width:248px;height:174px}
.card-title{position:absolute;top:3191px;width:248px;color:var(--white);font-family:"Roboto Condensed",sans-serif;font-size:19px;line-height:25px}
.card-meta{position:absolute;top:3250px;color:#cfcfcf;font-size:11.5px;display:flex;align-items:center;gap:6px}
.card-more{position:absolute;top:3287px;color:var(--yellow);font-family:"Roboto Condensed",sans-serif;font-weight:700;font-size:13px;border-bottom:1px solid var(--yellow);padding-bottom:4px;display:flex;align-items:center;gap:6px}

/* Footer */
.footer{position:absolute;left:0;top:3835px;width:1200px;height:422px;background:var(--footer);color:#cfcfcf}
.foot-head{position:absolute;top:3922px;color:var(--white);font-family:"Roboto Condensed",sans-serif;font-weight:700;font-size:16px}
.foot-link{position:absolute;font-size:14px;color:#cfcfcf}
.contact-item{position:absolute;left:866px;display:flex;gap:14px;font-size:14px;line-height:22px}
</style>
</head>
<body>

<!-- Hero -->
<div class="hero" role="img" aria-label="Snowy pine forest trail under a cloudy sky"></div>
<svg class="abs" style="left:0;top:560px" width="1200" height="82" viewBox="0 0 1200 82" aria-hidden="true">
  <path d="M0 30 C120 50 220 20 340 40 C480 62 620 28 760 44 C900 60 1040 20 1200 36 L1200 82 L0 82 Z" fill="#ffffff"/>
</svg>
<div class="nav-band"></div>
<a class="nav-link active" style="left:183px">Home</a>
<a class="nav-link" style="left:271px">About</a>
<a class="nav-link" style="left:367px">Services</a>
<a class="nav-link" style="left:464px">Offers</a>
<a class="nav-link" style="left:737px">Packages</a>
<a class="nav-link" style="left:843px">Reviews</a>
<a class="nav-link" style="left:931px">Blog</a>
<a class="nav-link" style="left:1018px">Contact</a>
<div class="brand"><span class="brand-dot"></span><span>Cedar Hollow<br>Drift Tours</span></div>
<h1 class="hero-title">CEDAR HOLLOW<br>DRIFT <span class="script">Tours</span></h1>
<div class="side-line" style="left:0"></div>
<div class="side-nav" style="left:66px;transform:rotate(90deg);transform-origin:left top;top:330px;left:84px">PREV</div>
<div class="side-line" style="left:1134px"></div>
<div class="side-nav" style="left:1102px;transform:rotate(-90deg);transform-origin:left top;top:362px">NEXT</div>

<!-- About -->
<div class="abs eyebrow" style="left:71px;top:771px">ABOUT</div>
<h2 class="about-title cond">CEDAR HOLLOW<br>DRIFT TOURS</h2>
<p class="about-text">Lorem ipsum dolor sit amet, consectetur adiiscing elit, sed do eiu tecididunt ut labore et dolore magna aliqua. Quis ipsum suspendisse ultrices gravida. Risus commodo viverra maecenas accumsan lacus vel facilisis.</p>
<a class="btn" style="left:521px;top:883px;width:183px;height:54px">Read More</a>

<!-- Services -->
<section class="services"></section>
<div class="outline-word" style="top:1130px;font-size:200px;-webkit-text-stroke:1.5px var(--outline-dark)">SERVICES</div>
<div class="abs center yellow-eyebrow" style="left:600px;top:1189px">WHAT WE SERVE</div>
<h2 class="abs center cond section-title" style="left:600px;top:1217px">WE PROVIDE TOP DESTINATIONS</h2>
<div class="dest" style="left:73px"><div class="dest-photo" role="img" aria-label="Skier on a snowy forest trail" style="background:radial-gradient(circle,#dfe4e8,#9aa4a6 70%,#5c6863)"></div></div>
<div class="dest" style="left:343px"><div class="dest-photo" role="img" aria-label="Snow-laden firs below a mountain ridge" style="background:linear-gradient(180deg,#b7c7d8,#5e6a70 45%,#e6eaee)"></div></div>
<div class="dest" style="left:612px"><div class="dest-photo" role="img" aria-label="Snowy mountain peak under a blue sky" style="background:linear-gradient(180deg,#2a5fa8,#5d8ccc 45%,#dfe6ee 70%,#6d7a86)"></div></div>
<div class="dest" style="left:881px"><div class="dest-photo" role="img" aria-label="Misty snowfield with a line of trees" style="background:linear-gradient(180deg,#b9bfc4,#a6adb2 60%,#5f6b6a 72%,#e4e7ea)"></div></div>
<div class="dest-name cond center" style="left:195px">Bear Creek - Upper</div>
<div class="dest-name cond center" style="left:465px">Castle</div>
<div class="dest-name cond center" style="left:734px">Electric Peak 2</div>
<div class="dest-name cond center" style="left:1003px">Mineral Hil</div>

<!-- Gallery -->
<div class="outline-word" style="top:1760px;font-size:200px;-webkit-text-stroke:1.5px var(--outline-light)">GALLERY</div>
<h2 class="abs center cond" style="left:600px;top:1826px;font-size:52px;color:var(--ink)">PHOTO GALLERY</h2>
<div class="gallery-photo" style="left:0;background:linear-gradient(90deg,#6e7a7b,#a8b0b4 45%,#3f4a47)" role="img" aria-label="Snow-covered pines in a quiet forest"></div>
<div class="gallery-photo" style="left:400px;background:linear-gradient(180deg,#8ea2a3 0%,#8ea2a3 40%,#d9a06a 55%,#9a6a45 75%,#3a3434)" role="img" aria-label="Mountain peak lit by golden sunset light"></div>
<div class="gallery-photo" style="left:800px;background:linear-gradient(90deg,#2f3634,#b3b9bc 50%,#4b5453)" role="img" aria-label="Foggy forest slope with snowy firs"></div>
<svg class="chev" style="left:68px" width="30" height="56" viewBox="0 0 30 56" aria-hidden="true"><path d="M28 2 L2 28 L28 54" fill="none" stroke="#ffffff" stroke-width="1.5"/></svg>
<svg class="chev" style="left:1102px" width="30" height="56" viewBox="0 0 30 56" aria-hidden="true"><path d="M2 2 L28 28 L2 54" fill="none" stroke="#ffffff" stroke-width="1.5"/></svg>

<!-- Testimonial -->
<svg class="abs" style="left:560px;top:2404px" width="80" height="50" viewBox="0 0 80 50" aria-hidden="true">
  <path d="M14 0 H32 L22 18 H32 V50 H2 V22 Z" fill="var(--yellow)"/>
  <path d="M54 0 H72 L62 18 H72 V50 H42 V22 Z" fill="var(--yellow)"/>
</svg>
<p class="quote">Lorem ipsum dolor sit amet, coetur adipiscing elit.<br>Nam eleifend lectus sit amla elementm, non interdum<br>lacus efficitur.</p>
<div class="abs center cond" style="left:600px;top:2617px;font-size:18px">Lorem ipsum, Dolor</div>
<div class="abs" style="left:528px;top:2676px;width:28px;height:1px;background:#444"></div>
<div class="abs cond" style="left:559px;top:2667px;font-size:15px;font-weight:400">PREV</div>
<div class="abs cond" style="left:607px;top:2667px;font-size:15px;font-weight:400">NEXT</div>
<div class="abs" style="left:646px;top:2676px;width:28px;height:1px;background:#444"></div>

<!-- Blog -->
<section class="blog"></section>
<div class="outline-word" style="top:2812px;font-size:150px;-webkit-text-stroke:1.5px var(--outline-dark)">BLOG</div>
<div class="abs center yellow-eyebrow" style="left:600px;top:2876px">LATEST BLOG POSTS</div>
<h2 class="abs center cond section-title" style="left:600px;top:2904px">OUR LATEST ARTICLE</h2>

<div class="card-photo" style="left:71px;background:linear-gradient(180deg,#e6ebee,#7d8a8a 45%,#f2f4f5 75%,#4c5a5e)" role="img" aria-label="Creek running through deep snow"></div>
<div class="card-photo" style="left:342px;background:linear-gradient(180deg,#2f70c4,#7fa6d8 40%,#eef2f6 70%,#ffffff)" role="img" aria-label="Skier standing below snowy mountains"></div>
<div class="card-photo" style="left:612px;background:linear-gradient(180deg,#d6dadd,#6b7677 50%,#e8ebed)" role="img" aria-label="Frosted pines over a valley"></div>
<div class="card-photo" style="left:883px;background:linear-gradient(160deg,#3c4b52,#c9d1d6 50%,#7b2f3a 65%,#eef1f3)" role="img" aria-label="Skier carving through fresh powder"></div>

<div class="card-title" style="left:71px">Quisque feugiat ultricies<br>nulla a pharetra</div>
<div class="card-title" style="left:342px">Quisque feugiat ultricies<br>nulla a pharetra</div>
<div class="card-title" style="left:612px">Quisque feugiat ultricies<br>nulla a pharetra</div>
<div class="card-title" style="left:883px">Quisque feugiat ultricies<br>nulla a pharetra</div>

<div class="card-meta" style="left:71px"><svg width="11" height="11" viewBox="0 0 12 12"><circle cx="6" cy="6" r="5" fill="none" stroke="var(--yellow)" stroke-width="1.4"/><path d="M6 3v3h2" fill="none" stroke="var(--yellow)" stroke-width="1.4"/></svg>20 Oct 2021<span style="width:16px"></span><svg width="13" height="11" viewBox="0 0 13 11"><path d="M1 1h11v7H5l-3 2V8H1z" fill="none" stroke="var(--yellow)" stroke-width="1.3"/></svg>21 Comments</div>
<div class="card-meta" style="left:342px"><svg width="11" height="11" viewBox="0 0 12 12"><circle cx="6" cy="6" r="5" fill="none" stroke="var(--yellow)" stroke-width="1.4"/><path d="M6 3v3h2" fill="none" stroke="var(--yellow)" stroke-width="1.4"/></svg>20 Oct 2021<span style="width:16px"></span><svg width="13" height="11" viewBox="0 0 13 11"><path d="M1 1h11v7H5l-3 2V8H1z" fill="none" stroke="var(--yellow)" stroke-width="1.3"/></svg>21 Comments</div>
<div class="card-meta" style="left:612px"><svg width="11" height="11" viewBox="0 0 12 12"><circle cx="6" cy="6" r="5" fill="none" stroke="var(--yellow)" stroke-width="1.4"/><path d="M6 3v3h2" fill="none" stroke="var(--yellow)" stroke-width="1.4"/></svg>20 Oct 2021<span style="width:16px"></span><svg width="13" height="11" viewBox="0 0 13 11"><path d="M1 1h11v7H5l-3 2V8H1z" fill="none" stroke="var(--yellow)" stroke-width="1.3"/></svg>21 Comments</div>
<div class="card-meta" style="left:883px"><svg width="11" height="11" viewBox="0 0 12 12"><circle cx="6" cy="6" r="5" fill="none" stroke="var(--yellow)" stroke-width="1.4"/><path d="M6 3v3h2" fill="none" stroke="var(--yellow)" stroke-width="1.4"/></svg>20 Oct 2021<span style="width:16px"></span><svg width="13" height="11" viewBox="0 0 13 11"><path d="M1 1h11v7H5l-3 2V8H1z" fill="none" stroke="var(--yellow)" stroke-width="1.3"/></svg>21 Comments</div>

<a class="card-more" style="left:71px">READ MORE <svg width="6" height="8" viewBox="0 0 6 8"><path d="M0 0l6 4-6 4z" fill="var(--yellow)"/></svg></a>
<a class="card-more" style="left:342px">READ MORE <svg width="6" height="8" viewBox="0 0 6 8"><path d="M0 0l6 4-6 4z" fill="var(--yellow)"/></svg></a>
<a class="card-more" style="left:612px">READ MORE <svg width="6" height="8" viewBox="0 0 6 8"><path d="M0 0l6 4-6 4z" fill="var(--yellow)"/></svg></a>
<a class="card-more" style="left:883px">READ MORE <svg width="6" height="8" viewBox="0 0 6 8"><path d="M0 0l6 4-6 4z" fill="var(--yellow)"/></svg></a>

<div class="abs" style="left:58px;top:3075px;width:40px;height:57px;background:rgba(255,255,255,.25)"></div>
<svg class="abs" style="left:64px;top:3089px" width="14" height="30" viewBox="0 0 14 30" aria-hidden="true"><path d="M13 1 L1 15 L13 29" fill="none" stroke="#ffffff" stroke-width="1.5"/></svg>
<div class="abs" style="left:1098px;top:3075px;width:59px;height:57px;background:var(--yellow)"></div>
<svg class="abs" style="left:1120px;top:3089px" width="14" height="30" viewBox="0 0 14 30" aria-hidden="true"><path d="M1 1 L13 15 L1 29" fill="none" stroke="#ffffff" stroke-width="1.5"/></svg>

<!-- Call -->
<div class="outline-word" style="top:3408px;font-size:200px;-webkit-text-stroke:1.5px var(--outline-light)">CALL US</div>
<h2 class="abs center cond" style="left:600px;top:3476px;font-size:52px;color:var(--ink)">CALL FOR A TOUR</h2>
<p class="abs center" style="left:600px;top:3608px;font-size:25px;line-height:36px;color:#2a2a2a">Give us a call anytime, we endeavour to answer<br>all enquiries</p>
<a class="btn" style="left:521px;top:3706px;width:183px;height:54px">Call Now</a>

<!-- Footer -->
<footer class="footer"></footer>
<div class="abs" style="left:75px;top:3900px;width:124px;height:124px;border-radius:50%;background:#dfe4ea"></div>
<div class="abs" style="left:214px;top:3944px;color:var(--white);font-size:15px;font-weight:500;line-height:20px">Cedar Hollow<br>Drift Tours</div>
<p class="abs" style="left:71px;top:4040px;width:260px;font-size:13.5px;line-height:23px;color:#cfcfcf">Lorem ipsum dolor s consectetur adiiscing elit, sed do eiu tecididunt ut labore et dolore magna aliqua. Quis ipsum suspendisse ultrices gravida.</p>

<div class="foot-head" style="left:364px">USEFUL LINKS</div>
<a class="foot-link" style="left:365px;top:3976px">Home</a>
<a class="foot-link" style="left:365px;top:4015px">About</a>
<a class="foot-link" style="left:365px;top:4057px">Services</a>
<a class="foot-link" style="left:365px;top:4098px">Offers Packages</a>
<a class="foot-link" style="left:491px;top:3976px">Reviews</a>
<a class="foot-link" style="left:491px;top:4015px">Blog</a>
<a class="foot-link" style="left:491px;top:4057px">Contact</a>

<div class="foot-head" style="left:636px">SUPPORT</div>
<a class="foot-link" style="left:637px;top:3976px">Customer Support</a>
<a class="foot-link" style="left:637px;top:4015px">Privacy &amp; Policy</a>
<a class="foot-link" style="left:637px;top:4057px">Terms &amp; Condition</a>
<a class="foot-link" style="left:637px;top:4098px">Tour Guid</a>

<div class="foot-head" style="left:866px">CONTACT INFO</div>
<div class="contact-item" style="top:3974px"><svg width="10" height="14" viewBox="0 0 10 14" style="margin-top:3px"><path d="M5 0C2.2 0 0 2.2 0 5c0 3.5 5 9 5 9s5-5.5 5-9c0-2.8-2.2-5-5-5zm0 7a2 2 0 110-4 2 2 0 010 4z" fill="var(--yellow)"/></svg><span>12 Ridgeline Road,<br>Gardiner Valley, MT</span></div>
<div class="contact-item" style="top:4028px"><svg width="12" height="12" viewBox="0 0 12 12" style="margin-top:5px"><path d="M2.5 0.5l2 2.5-1.2 1.5c.8 1.6 2 2.8 3.7 3.7L8.5 7l2.5 2-1 2c-5 0-9.5-4.5-9.5-9.5z" fill="var(--yellow)"/></svg><span>01 555 210 448</span></div>
<div class="contact-item" style="top:4062px"><svg width="12" height="10" viewBox="0 0 12 10" style="margin-top:6px"><rect width="12" height="10" fill="var(--yellow)"/><path d="M0 0l6 5 6-5" fill="none" stroke="var(--footer)" stroke-width="1.2"/></svg><span>info@cedarhollowdrifttours</span></div>

<div class="abs" style="left:71px;top:4195px;width:1058px;height:1px;background:#444"></div>
<div class="abs center" style="left:600px;top:4216px;font-family:'Roboto Condensed',sans-serif;font-size:12px;color:#9a9a9a">© 2021 <span style="color:var(--white)">Cedar Hollow Drift Tours.</span> All right reserved</div>

</body>
</html>
```